"Rise. Shift. Thrive." Empowerment Book Cover

Hello, I need a hot, trendy, and contemporary book cover designed for my first book called "Rise. Shift. Thrive. -- 360 Bold Momentum Notes to Guide Anyone to Rise, Shift, and Thrive in Their Career & Daily Dreams."
This is my first book and I am really wanting to launch my brand with it... it would be awesome to match the inside/outside branding of the book. So we can either create the book cover to match the book guts, or update the book guts to match the cover.
Lastly, I just got a professional photoshoot done last week so we can use one of those images, or we can go with a different idea/style for the cover. The body of the book is attached. All questions welcomed, happy designing!
Target Market(s)
Gen Z, Millennials and Gen X.
Industry/Entity Type
Personal Development.
Requirements
Must have
- It must stand out and be different from other typical book covers.
Nice to have
- Success, Inspiration, Motivation, Mindset, Growth.
Should not have
- Clipart, stock art, stock look and feel.

```html
<!DOCTYPE html>
<html lang="en">
<head>
<meta charset="utf-8">
<title>Rise. Shift. Thrive. — Book Cover</title>
<link rel="stylesheet" href="https://fonts.googleapis.com/css2?family=Questrial&display=swap">
<style>
  :root {
    --page-bg: #f3f0ef;
    --cover-blue: #0a57b0;
    --cover-navy: #06346f;
    --title-light: #bfe3ff;
    --title-mid: #1a90d9;
    --title-dark: #06306a;
    --subtitle: #8fcaf5;
    --author: #ffffff;
    --portrait-light: #24467f;
    --portrait-deep: #0f2a5a;
  }
  * { margin: 0; padding: 0; box-sizing: border-box; }
  html, body {
    width: 1200px;
    height: 895px;
    overflow: hidden;
    background: var(--page-bg);
  }
  .canvas {
    position: relative;
    width: 1200px;
    height: 895px;
  }
  .cover {
    position: absolute;
    left: 360px;
    top: 20px;
    width: 480px;
    height: 855px;
    overflow: hidden;
    border-radius: 18px;
    font-family: "Questrial", "Century Gothic", sans-serif;
    box-shadow: 0 10px 30px rgba(0, 0, 0, 0.18);
  }
  .cover-art {
    position: absolute;
    inset: 0;
    width: 100%;
    height: 100%;
  }
  .title {
    position: absolute;
    left: 28px;
    top: 46px;
    font-weight: 400;
    font-size: 98px;
    line-height: 90px;
    letter-spacing: 1px;
  }
  .title span { display: block; }
  .title .word-rise { color: var(--title-light); }
  .title .word-shift { color: var(--title-mid); }
  .title .word-thrive { color: var(--title-dark); }
  .subtitle {
    position: absolute;
    left: 32px;
    top: 402px;
    color: var(--subtitle);
    font-size: 20px;
    line-height: 28px;
  }
  .subtitle .lead {
    display: block;
    font-size: 26px;
    line-height: 31px;
    margin-bottom: 2px;
  }
  .author {
    position: absolute;
    left: 36px;
    top: 700px;
    color: var(--author);
    font-size: 31px;
    line-height: 39px;
  }
</style>
</head>
<body>
  <main class="canvas">
    <section class="cover">
      <svg class="cover-art" viewBox="0 0 480 855" xmlns="http://www.w3.org/2000/svg">
        <defs>
          <linearGradient id="portraitTone" x1="0" y1="0" x2="0.4" y2="1">
            <stop offset="0" stop-color="var(--portrait-light)"/>
            <stop offset="1" stop-color="var(--portrait-deep)"/>
          </linearGradient>
        </defs>
        <rect class="band-upper" x="0" y="0" width="480" height="855" fill="var(--cover-blue)"/>
        <polygon class="band-lower" points="0,386 480,332 480,855 0,855" fill="var(--cover-navy)"/>
        <path class="author-portrait" role="img" aria-label="Portrait photo of the author in a navy suit, seated and smiling"
              d="M320 322 H480 V855 H190 V650 Q190 560 270 540 V370 Q270 322 320 322 Z"
              fill="url(#portraitTone)"/>
      </svg>

      <h1 class="title">
        <span class="word-rise">Rise.</span>
        <span class="word-shift">Shift.</span>
        <span class="word-thrive">Thrive.</span>
      </h1>

      <p class="subtitle">
        <span class="lead">360 Bold<br>Momentum Notes</span>
        to Guide Anyone to Rise,<br>Shift, and Thrive in<br>Their Career &amp;<br>Daily Dreams.
      </p>

      <p class="author">Samir<br>Castellano</p>
    </section>
  </main>
</body>
</html>
```